Bref créative
Business cards, stationery, powerpoint template, and email signature for business consulting firm
Bellwether Advisory Group The Ground Level Method
Simple
Corwin Pike
Consultant
PO Box 7086
Brindle, OR 97512
cpike@bellwethgrp.net
We will be adding new employees so I would like the business card file to be changeable. I would like to see both one sided and two-sided business cards.
The logo files will have all parts of the logo available both separate and complete.
This is the complete logo
This is the file with the logo components

```html
<!DOCTYPE html>
<html lang="en">
<head>
<meta charset="utf-8">
<title>Bellwether Advisory Group – Business Card</title>
<link rel="stylesheet" href="https://fonts.googleapis.com/css2?family=Cinzel:wght@400;600&display=swap">
<style>
  :root {
    --backdrop: #e4e2df;
    --card: #ffffff;
    --ink: #3a3a3c;
    --muted: #55565a;
    --accent: #5b2a86;
    --icon: #3d3d40;
    --mark: #6a9a2e;
  }
  * { margin: 0; padding: 0; box-sizing: border-box; }
  html, body {
    width: 1200px;
    height: 900px;
    overflow: hidden;
    background: var(--backdrop);
  }
  .card {
    position: absolute;
    left: 100px;
    top: 164px;
    width: 1000px;
    height: 572px;
    background: var(--card);
    box-shadow: 0 6px 24px rgba(0,0,0,0.12);
    font-family: "Cinzel", serif;
    color: var(--ink);
  }
  .brand {
    position: absolute;
    left: 72px;
    top: 92px;
  }
  .brand-row {
    display: flex;
    align-items: center;
    gap: 18px;
  }
  .brand-dot {
    width: 54px;
    height: 54px;
    border-radius: 50%;
    background: var(--mark);
    flex: none;
  }
  .brand-name {
    font-size: 36px;
    font-weight: 600;
    color: var(--ink);
    letter-spacing: 0.5px;
    line-height: 1;
  }
  .brand-tagline {
    margin: 12px 0 0 72px;
    font-size: 15px;
    letter-spacing: 5px;
    color: var(--muted);
    text-transform: uppercase;
  }
  .contact {
    position: absolute;
    left: 72px;
    top: 334px;
    list-style: none;
    font-size: 20px;
    color: var(--muted);
    line-height: 1.2;
  }
  .contact li {
    display: flex;
    align-items: flex-start;
    gap: 12px;
    margin-bottom: 6px;
  }
  .contact .icon {
    width: 18px;
    height: 18px;
    flex: none;
    margin-top: 3px;
  }
  .contact .no-icon { width: 18px; flex: none; }
  .person {
    position: absolute;
    right: 72px;
    top: 360px;
    text-align: right;
  }
  .person-name {
    font-size: 26px;
    font-weight: 600;
    color: var(--accent);
    letter-spacing: 1px;
  }
  .person-role {
    font-size: 19px;
    color: var(--muted);
    margin-top: 4px;
  }
</style>
</head>
<body>
  <div class="card">
    <div class="brand">
      <div class="brand-row">
        <span class="brand-dot"></span>
        <span class="brand-name">Bellwether Advisory Group</span>
      </div>
      <p class="brand-tagline">The Ground Level Method</p>
    </div>

    <ul class="contact">
      <li>
        <svg class="icon" viewBox="0 0 18 18" aria-hidden="true"><circle cx="9" cy="9" r="9" fill="var(--icon)"/><path d="M4.5 9.2 9 5.2l4.5 4H12v3.6H6V9.2z" fill="#fff"/></svg>
        <span>PO Box 7086 Brindle,</span>
      </li>
      <li>
        <span class="no-icon"></span>
        <span>OR 97512</span>
      </li>
      <li>
        <svg class="icon" viewBox="0 0 18 18" aria-hidden="true"><circle cx="9" cy="9" r="9" fill="var(--icon)"/><path d="M6 4.5c.6 0 1.4 1.8 1.4 2.2s-.9.8-.8 1.2c.3 1 1.3 2 2.3 2.3.4.1.8-.8 1.2-.8s2.2.8 2.2 1.4-.9 1.7-1.8 1.7C7.6 12.5 5.5 10.4 5.5 7.5c0-1 .1-3 .5-3z" fill="#fff"/></svg>
        <span>503-555-0183</span>
      </li>
      <li>
        <svg class="icon" viewBox="0 0 18 18" aria-hidden="true"><circle cx="9" cy="9" r="9" fill="var(--icon)"/><rect x="4.5" y="6" width="9" height="6.2" fill="#fff"/><path d="M4.5 6 9 9.5 13.5 6" fill="none" stroke="var(--icon)" stroke-width="1"/></svg>
        <span>cpike@bellwethgrp.net</span>
      </li>
      <li>
        <svg class="icon" viewBox="0 0 18 18" aria-hidden="true"><circle cx="9" cy="9" r="9" fill="var(--icon)"/><circle cx="9" cy="9" r="4.5" fill="none" stroke="#fff" stroke-width="1.2"/><ellipse cx="9" cy="9" rx="2" ry="4.5" fill="none" stroke="#fff" stroke-width="1"/><path d="M4.5 9h9" stroke="#fff" stroke-width="1"/></svg>
        <span>www.bellwethgrp.net</span>
      </li>
    </ul>

    <div class="person">
      <p class="person-name">Corwin Pike</p>
      <p class="person-role">Consultant</p>
    </div>
  </div>
</body>
</html>
```